Copper wren builds

Copper wren builds is a small construction company.
Who is a licenced builder, Carpenter, joiner,
working on heritage ,new build, speacial projects and sometimes furniture

Industry/Entity Type

Construction

```html
<!DOCTYPE html>
<html lang="en">
<head>
<meta charset="UTF-8">
<title>Copper wren builds — Business Card</title>
<link href="https://fonts.googleapis.com/css2?family=Oswald:wght@600&family=Roboto:wght@300;400&display=swap" rel="stylesheet">
<style>
  :root {
    --page-bg: #e9e9e9;
    --card-light: #474747;
    --card-dark: #141414;
    --brand-green: #5fbf6a;
    --text-light: #f2f2f2;
    --divider: #9a9a9a;
  }
  * { margin: 0; padding: 0; box-sizing: border-box; }
  html, body {
    width: 1200px;
    height: 900px;
    overflow: hidden;
    background: var(--page-bg);
  }
  .canvas {
    position: relative;
    width: 1200px;
    height: 900px;
    display: flex;
    align-items: center;
    justify-content: center;
  }
  .business-card {
    position: relative;
    width: 1000px;
    height: 580px;
    border-radius: 26px;
    background: radial-gradient(ellipse 70% 80% at 38% 38%, var(--card-light) 0%, #2e2e2e 45%, var(--card-dark) 100%);
    box-shadow: 0 18px 40px rgba(0, 0, 0, 0.25);
    overflow: hidden;
  }
  .company-name {
    position: absolute;
    top: 170px;
    left: 0;
    width: 100%;
    padding-left: 180px;
    text-align: center;
    font-family: 'Oswald', sans-serif;
    font-weight: 600;
    font-size: 76px;
    letter-spacing: -1px;
    color: var(--brand-green);
  }
  .contact-row {
    position: absolute;
    top: 365px;
    left: 230px;
    display: flex;
    align-items: center;
  }
  .person {
    text-align: right;
  }
  .person-name {
    font-family: 'Oswald', sans-serif;
    font-weight: 600;
    font-size: 54px;
    line-height: 1.1;
    color: var(--brand-green);
  }
  .person-role {
    font-family: 'Roboto', sans-serif;
    font-weight: 300;
    font-size: 30px;
    color: var(--text-light);
  }
  .divider {
    width: 3px;
    height: 90px;
    margin: 30px 34px 0 38px;
    background: var(--divider);
  }
  .contact-list {
    list-style: none;
    margin-top: 40px;
  }
  .contact-item {
    display: flex;
    align-items: center;
    gap: 14px;
    font-family: 'Roboto', sans-serif;
    font-weight: 400;
    font-size: 30px;
    color: var(--text-light);
    line-height: 1.35;
  }
  .contact-icon {
    width: 28px;
    height: 28px;
    flex-shrink: 0;
    fill: var(--brand-green);
  }
</style>
</head>
<body>
  <main class="canvas">
    <section class="business-card">
      <h1 class="company-name">Copper wren builds</h1>

      <div class="contact-row">
        <div class="person">
          <p class="person-name">Miles Harrow</p>
          <p class="person-role">Owner</p>
        </div>

        <span class="divider"></span>

        <ul class="contact-list">
          <li class="contact-item">
            <svg class="contact-icon" viewBox="0 0 24 24" aria-hidden="true">
              <path d="M6.6 10.8c1.4 2.8 3.8 5.1 6.6 6.6l2.2-2.2c.3-.3.7-.4 1-.2 1.1.4 2.3.6 3.6.6.6 0 1 .4 1 1V20c0 .6-.4 1-1 1C10.6 21 3 13.4 3 4c0-.6.4-1 1-1h3.5c.6 0 1 .4 1 1 0 1.3.2 2.5.6 3.6.1.3 0 .7-.2 1l-2.3 2.2z"/>
            </svg>
            <span>555 014 2290</span>
          </li>
          <li class="contact-item">
            <svg class="contact-icon" viewBox="0 0 24 24" aria-hidden="true">
              <path d="M2 5h20v14H2z M2 5l10 8 10-8" fill="var(--brand-green)"/>
              <path d="M2 5l10 8 10-8" fill="none" stroke="#1e1e1e" stroke-width="1.6"/>
            </svg>
            <span>hello@copperwren.com</span>
          </li>
        </ul>
      </div>
    </section>
  </main>
</body>
</html>
```